Loyalty/Gift Card Design-

RimTallow needs a design for a loyalty card for a retail gas discount program. The card will need to fit specifications for plumvex cards cr-80 magnetic card found on www.plumvexcards.example

The way our program works is a consumer will see advertisement for our program and come to a local gas station to purchase our RimTallow Card. It will be a set price up- front, then our program/card will save consumers 15 cents per gallon on 100 gallons of fuel. Once the 100 gallons is used the customer will have the option of reloading (for another set cost) another 100 gallons on the card to receive another 15 cents off on next 100 gallons.

Key Info to Incorporate on card--
"Save 15 cents per gallon on next 100 gallons of fuel"
Never pay full price on fuel again!
"Card Valid Only At" (then a space for our stores name and address)
Brought to you by-- RimTallow Name & Logo

Target Market(s)

Consumers conscious of gas prices/ economy who are looking to save money where they can. We are looking for a design that fits "big box" theme, with very clean design.

Industry/Entity Type

Gas Station

Requirements
Must have
• Colors Red,, Blue, White--
Sell Message of Saving and Value.
Should not have
• Designs with fuel pumps

```html
<!DOCTYPE html>
<html lang="en">
<head>
<meta charset="utf-8">
<title>RimTallow Fuel Savings Card</title>
<link rel="stylesheet" href="https://fonts.googleapis.com/css2?family=Bebas+Neue&family=Questrial&family=Nunito:wght@300;400&display=swap">
<style>
  :root {
    --red: #e3001b;
    --red-soft: #ec2a3c;
    --blue: #0a2d8f;
    --white: #ffffff;
    --black: #000000;
    --metal-light: #eceef0;
    --metal-mid: #d6d8db;
    --metal-dark: #c4c7cb;
    --page: #efefef;
    --ink: #2a2a2a;
  }
  html, body {
    margin: 0;
    padding: 0;
    width: 900px;
    height: 1200px;
    overflow: hidden;
    background: var(--page);
  }
  .canvas {
    position: relative;
    width: 900px;
    height: 1200px;
  }
  .card {
    position: absolute;
    left: 70px;
    width: 762px;
    height: 480px;
    border-radius: 22px;
    overflow: hidden;
    background: linear-gradient(100deg, var(--metal-mid) 0%, var(--metal-light) 35%, var(--metal-mid) 60%, var(--metal-light) 85%, var(--metal-dark) 100%);
    box-shadow: 0 2px 6px rgba(0,0,0,0.15);
  }
  .card-front { top: 60px; }
  .card-back { top: 660px; }

  .tagline {
    position: absolute;
    left: 0; right: 0;
    top: 20px;
    text-align: center;
    font-family: "Questrial", sans-serif;
    font-weight: 400;
    font-size: 43px;
    color: var(--blue);
    margin: 0;
  }
  .front-art { position: absolute; inset: 0; }

  .offer {
    position: absolute;
    left: 38px;
    top: 236px;
    font-family: "Bebas Neue", sans-serif;
    color: var(--white);
    line-height: 1;
  }
  .offer-lead { font-size: 24px; letter-spacing: 0.5px; }
  .offer-save { font-size: 92px; margin-top: 2px; line-height: 0.85; }
  .offer-amount { display: flex; align-items: flex-end; margin-top: 4px; }
  .offer-number { font-size: 138px; line-height: 0.78; }
  .offer-unit { font-size: 23px; line-height: 0.95; margin-left: 6px; margin-bottom: 2px; }

  .drop-text {
    position: absolute;
    left: 430px;
    top: 300px;
    width: 130px;
    text-align: center;
    font-family: "Bebas Neue", sans-serif;
    color: var(--blue);
    line-height: 0.9;
    transform: rotate(-22deg);
  }
  .drop-lead { font-size: 24px; }
  .drop-number { font-size: 72px; }
  .drop-unit { font-size: 20px; }

  .question {
    position: absolute;
    left: 614px;
    top: 62px;
    font-family: "Bebas Neue", sans-serif;
    font-size: 300px;
    line-height: 1;
    color: var(--blue);
  }

  .mag-stripe {
    position: absolute;
    left: 0; right: 0;
    top: 48px;
    height: 108px;
    background: var(--black);
  }
  .message-band {
    position: absolute;
    left: 0; right: 0;
    top: 158px;
    height: 172px;
    background: linear-gradient(90deg, var(--red) 0 467px, var(--blue) 467px 100%);
  }
  .signature-panel {
    position: absolute;
    left: 42px;
    top: 18px;
    width: 677px;
    height: 88px;
    background: var(--white);
  }
  .slogan {
    position: absolute;
    left: 41px;
    top: 122px;
    margin: 0;
    font-family: "Bebas Neue", sans-serif;
    font-size: 39px;
    color: var(--white);
    white-space: nowrap;
    letter-spacing: 0.3px;
  }
  .slogan-end { position: absolute; left: 435px; }
  .fine-print {
    position: absolute;
    top: 338px;
    margin: 0;
    font-family: "Nunito", sans-serif;
    font-weight: 300;
    font-size: 19px;
    color: var(--ink);
  }
  .valid-at { left: 42px; }
  .brought-by { left: 480px; }
  .sponsor {
    position: absolute;
    left: 482px;
    top: 384px;
    display: flex;
    align-items: center;
    gap: 10px;
  }
  .sponsor-mark {
    width: 34px;
    height: 34px;
    background: var(--blue);
  }
  .sponsor-name {
    font-family: "Bebas Neue", sans-serif;
    font-size: 52px;
    color: var(--blue);
    line-height: 1;
  }
</style>
</head>
<body>
<main class="canvas">

  <section class="card card-front" aria-label="Card front">
    <h1 class="tagline">A passport for better life</h1>

    <svg class="front-art" width="762" height="480" viewBox="0 0 762 480">
      <defs>
        <linearGradient id="hand-fill" x1="0" y1="0" x2="1" y2="1">
          <stop offset="0" stop-color="var(--red)"/>
          <stop offset="1" stop-color="var(--red-soft)"/>
        </linearGradient>
      </defs>
      <path class="offer-panel" fill="var(--red)"
        d="M0 216 C80 206 160 196 240 182 L240 250 C236 320 240 390 258 440 C266 462 262 476 250 480 L0 480 Z"/>
      <rect class="hand-area" role="img" aria-label="Illustration of a red hand pinching a fuel drop"
        x="222" y="92" width="200" height="150" rx="40" fill="url(#hand-fill)"/>
      <path class="fuel-drop" fill="var(--white)"
        d="M412 232 C452 270 560 305 570 372 C578 422 540 452 495 448 C445 444 418 402 428 352 C436 312 422 272 412 232 Z"/>
      <circle class="coin" cx="671" cy="356" r="14" fill="var(--blue)"/>
      <text x="671" y="362" text-anchor="middle" font-family="Nunito, sans-serif" font-size="17" fill="var(--white)">¢</text>
      <rect class="piggy-area" role="img" aria-label="Red piggy bank illustration" x="620" y="380" width="102" height="52" rx="22" fill="var(--red)"/>
    </svg>

    <div class="question" aria-hidden="true">?</div>

    <div class="offer">
      <div class="offer-lead">What if you can</div>
      <div class="offer-save">Save</div>
      <div class="offer-amount">
        <span class="offer-number">15</span>
        <span class="offer-unit">Cents<br>per<br>gallon</span>
      </div>
    </div>

    <div class="drop-text">
      <div class="drop-lead">On next</div>
      <div class="drop-number">100</div>
      <div class="drop-unit">Gallons<br>of fuel</div>
    </div>
  </section>

  <section class="card card-back" aria-label="Card back">
    <div class="mag-stripe"></div>
    <div class="message-band">
      <div class="signature-panel"></div>
      <p class="slogan">Never pay full price on fuel <span class="slogan-end">again!</span></p>
    </div>
    <p class="fine-print valid-at">Card Valid Only At</p>
    <p class="fine-print brought-by">Brought to you by</p>
    <div class="sponsor">
      <span class="sponsor-mark"></span>
      <span class="sponsor-name">RimTallow</span>
    </div>
  </section>

</main>
</body>
</html>
```